Flyer needed for Seminar

Hello,
We are looking for eye-catching, inspiring marketing material for an educational seminar. We need 4 x 6 clubcards with the following info:

CLUBCARD FRONT:

Verander Academy Presents:

Stillness: Under The Surface
Unlock the hidden treasures of prayer
By. Shaykh Idris Kamal Al-Furati

Dates:Jan 23-25, 2015
Timings: Fri - 7pm - 9:30 pm; Sat/Sun - 9am - 8 pm

Location: Riverbend Grand Suites at Oakhaven Square
4385 Millbrook Lane, Plano, TX 75093

Seating is Limited. Register Today!
www.VeranderAcademy,com

CLUBCARD BACK:
In this unique seminar, learn how to connect spiritually with your Creator through prayer. Let us teach you the hidden meanings behind salah and why it is essential to your existence. Not only will the instructor impart the skills you'll need to master khushoo but he will delve more deeply, into the inner realms and intricacies of this ibadaa. As a result, the prayer will no longer be regarded as a mechanical chore, but an intimate meeting with the Divine. Through such insight, we hope you will leave this non-fiqh seminar with an awakened and unparalleled understanding of this fundamental pillar of Islam.

www.VeranderAcademy.com
For more info: Email - info@veranderacademy.com; Phone - 1-877-Verand4

Reason: I really appreciate all the submissions but am looking for something more eye-catching, something that really stirs ones interest and relates to the title of the seminar. Thank you!

```html
<!DOCTYPE html>
<html lang="en">
<head>
<meta charset="utf-8">
<title>Stillness: Under The Surface – Seminar Clubcards</title>
<link href="https://fonts.googleapis.com/css2?family=Cinzel:wght@400;600&family=PT+Sans:wght@400;700&family=Tinos:wght@400;700&family=Open+Sans:wght@400;700&display=swap" rel="stylesheet">
<style>
:root{
  --bg:#e6e6e6;
  --orange:#f2b13e;
  --orange-deep:#e98a1f;
  --tab-orange:#f26b1d;
  --green:#187a3c;
  --green-dark:#174a2c;
  --black:#0b0b0b;
  --silhouette:#050505;
  --yellow:#ffe600;
  --white:#ffffff;
  --silver-top:#ffffff;
  --silver-bottom:#6e6e6e;
}
*{margin:0;padding:0;box-sizing:border-box}
html,body{width:1200px;height:1000px;overflow:hidden;background:var(--bg)}
.canvas{position:relative;width:1200px;height:1000px}
.card{position:absolute;top:142px;width:478px;height:716px;overflow:hidden;box-shadow:0 10px 14px rgba(0,0,0,.25)}
.card--front{left:100px;background:var(--orange)}
.card--back{left:622px;background:var(--black)}
.abs{position:absolute}
.title{font-family:"Cinzel",serif;font-weight:400;letter-spacing:1px;line-height:1;
  background:linear-gradient(var(--silver-top) 20%,#c9c9c9 55%,var(--silver-bottom));
  -webkit-background-clip:text;background-clip:text;color:transparent;white-space:nowrap}
.tagline-bar{font-family:"PT Sans",sans-serif;letter-spacing:3px;text-align:center;font-size:20px;line-height:26px}
.subtitle{font-family:"Tinos",serif;font-size:17px;line-height:19px;white-space:nowrap}
.subtitle b{font-weight:700}
.sans{font-family:"Open Sans",sans-serif}
.dotted{border-top:2px dotted rgba(255,255,255,.8)}

/* front */
.presents{left:122px;top:0;width:234px;height:42px;background:var(--green);color:var(--white);font-size:17px;text-align:center;line-height:46px}
.figure-area{left:132px;top:95px;width:206px;height:240px;border-radius:100px 100px 20px 20px;background:linear-gradient(180deg,#e08a2a,#b9621a)}
.front-title{left:0;width:478px;text-align:center;top:340px;font-size:74px}
.front-tagline{left:76px;top:419px;width:324px;background:var(--orange-deep);color:var(--black)}
.front-sub{left:0;width:478px;top:451px;text-align:center;color:var(--white)}
.info-band{left:0;top:498px;width:478px;height:188px;background:var(--green)}
.info-band .strip{left:0;top:0;width:18px;height:188px;background:var(--green-dark)}
.info-band .rule{left:20px;top:0;width:5px;height:188px;background:var(--orange)}
.dates{left:55px;top:10px;color:var(--yellow);font-weight:700;font-size:17px}
.day{top:35px;width:118px;height:28px;background:var(--tab-orange);color:var(--white);font-size:17px;text-align:center;line-height:28px}
.time{top:63px;width:118px;height:27px;background:var(--black);color:var(--white);font-size:13px;text-align:center;line-height:27px}
.venue{left:55px;top:100px;color:var(--white);font-size:16.5px;line-height:24px;white-space:nowrap}
.venue b{color:var(--yellow)}
.limited{left:55px;top:158px;color:var(--yellow);font-weight:700;font-size:14.5px}
.web-band{left:0;top:686px;width:478px;height:30px;background:#f6c457;color:#2b2b2b;font-family:"PT Sans",sans-serif;font-weight:700;font-size:17px;letter-spacing:4px;line-height:30px;padding-left:60px}

/* back */
.back-top{left:0;top:0;width:478px;height:183px;background:var(--orange)}
.back-title{left:24px;top:22px;font-size:66px}
.back-tagline{left:27px;top:103px;width:322px;background:var(--black);color:var(--orange)}
.back-sub{left:27px;top:137px;color:var(--black)}
.back-green{left:0;top:183px;width:478px;height:375px;background:var(--green)}
.back-strip{left:0;top:558px;width:478px;height:38px;background:var(--orange)}
.silhouette-area{left:0;top:0}
.copy{left:32px;top:230px;color:var(--white);font-family:"PT Sans",sans-serif;font-size:13px;line-height:16px;white-space:nowrap}
.copy p{margin-bottom:16px}
.contact{left:27px;top:612px;color:var(--white);font-family:"PT Sans",sans-serif;font-size:14px;line-height:18px}
</style>
</head>
<body>
<div class="canvas">

  <section class="card card--front">
    <svg class="abs" style="left:0;top:0" width="478" height="716" viewBox="0 0 478 716" aria-hidden="true">
      <path d="M40,498 V240 H8 V215 H40 C40,150 90,112 150,98 C190,72 225,48 239,42 C253,48 288,72 328,98 C388,112 438,150 438,215 H470 V240 H438 V498 Z" fill="#0b0b0b"/>
      <path d="M458,686 L478,686 L478,660 Z" fill="#187a3c"/>
    </svg>
    <div class="abs sans presents">Verander Academy Presents:</div>
    <div class="abs figure-area" role="img" aria-label="Patterned silhouette of a person in prayer framed by the arch"></div>
    <h1 class="abs title front-title">STILLNESS</h1>
    <div class="abs tagline-bar front-tagline">UNDER THE SURFACE</div>
    <p class="abs subtitle front-sub">Unlock the hidden treasures of prayer<br><b>By. Shaykh Idris Kamal Al-Furati</b></p>

    <div class="abs info-band sans">
      <div class="abs strip"></div><div class="abs rule"></div>
      <div class="abs dotted" style="left:40px;top:5px;width:420px"></div>
      <div class="abs dates">Dates: Jan 23-25, 2015</div>
      <div class="abs day" style="left:55px">Friday</div>
      <div class="abs time" style="left:55px">7 pm - 9:30 pm</div>
      <div class="abs day" style="left:183px">Sat &amp; Sun</div>
      <div class="abs time" style="left:183px">9 am - 8 pm</div>
      <div class="abs dotted" style="left:40px;top:97px;width:420px"></div>
      <p class="abs venue"><b>Riverbend Grand Suites</b> at Oakhaven Square<br>4385 Millbrook Lane, Plano, TX 75093</p>
      <div class="abs dotted" style="left:40px;top:152px;width:420px"></div>
      <div class="abs limited">Seating is Limited. Register Today...!!!</div>
      <div class="abs dotted" style="left:40px;top:182px;width:420px"></div>
    </div>
    <div class="abs web-band">www.VeranderAcademy.com</div>
  </section>

  <section class="card card--back">
    <div class="abs back-top"></div>
    <h2 class="abs title back-title">STILLNESS</h2>
    <div class="abs tagline-bar back-tagline">UNDER THE SURFACE</div>
    <p class="abs subtitle back-sub">Unlock the hidden treasures of prayer<br><b>By. Shaykh Idris Kamal Al-Furati</b></p>
    <div class="abs back-green">
      <div class="abs dotted" style="left:15px;top:22px;width:450px"></div>
      <div class="abs dotted" style="left:15px;top:358px;width:450px"></div>
    </div>
    <div class="abs back-strip"></div>
    <svg class="abs silhouette-area" width="478" height="716" viewBox="0 0 478 716" role="img" aria-label="Dark silhouette of a man seated in prayer">
      <path d="M478,143 H400 C360,143 334,175 334,225 V395 C334,415 320,430 300,445 L246,482 C234,492 228,505 228,525 V596 H478 Z" fill="var(--silhouette)"/>
    </svg>
    <div class="abs copy">
      <p>In this unique seminar, learn how to connect<br>spiritually with your Creator through prayer.<br>Let us teach you the hidden meanings behind<br>salah and why it is essential to your existence.</p>
      <p>Not only will the instructor impart the skills you'll need<br>to master khushoo but he will delve more deeply,<br>into the inner realms and intricacies of this ibadaa.</p>
      <p>As a result, the prayer will no longer be regarded<br>as a mechanical chore, but an intimate meeting<br>with the Divine.</p>
      <p>Through such insight, we hope you will<br>leave this non-fiqh seminar with<br>an awakened and unparalleled<br>understanding of this<br>fundamental pillar of Islam.</p>
    </div>
    <p class="abs contact">Seating is Limited. Register Today!<br><b>www.VeranderAcademy.com</b><br>For more info:<br>Email - info@veranderacademy.com<br>Phone - 1-877-Verand4</p>
  </section>

</div>
</body>
</html>
```